KVT Business Cards

We require business cards for our business. We would like a matte black back to the card, with our logo centred in the middle. The front side of the card is open to design.

Target Market(s)

Clients looking for legal services (professional)

Industry/Entity Type

Legal

Contact Information for Business Card

Boris Telemark
Partner
Mobile: 0438 715 642
Email: boris@kvtlaw.co
Website: www.kvtlaw.co
Level 3, 118 Wexbury Street
Sydney NSW 2000

Font styles to use
Other font styles liked:
• Avenir

Colors
f04a50
ffffff
1b1b1b

Requirements
Must have
• Black back with logo included in the centre of the card.
• Our font is Avenir.

```html
<!DOCTYPE html>
<html lang="en">
<head>
<meta charset="utf-8">
<title>KVT Legal – Business Cards</title>
<link rel="stylesheet" href="https://fonts.googleapis.com/css2?family=Lato:wght@400;700;900&display=swap">
<style>
  :root {
    --page: #ecebe8;
    --card-black: #1f1c1d;
    --card-white: #ffffff;
    --crimson: #b3194a;
    --ink: #1b1b1b;
    --ink-soft: #3a3a3a;
    --shadow: rgba(0, 0, 0, 0.18);
  }
  * { box-sizing: border-box; margin: 0; padding: 0; }
  html, body {
    width: 1200px;
    height: 900px;
    overflow: hidden;
    background: var(--page);
    font-family: "Lato", "Avenir", sans-serif;
  }
  .canvas {
    position: relative;
    width: 1200px;
    height: 900px;
  }
  .card {
    position: absolute;
    width: 560px;
    height: 342px;
    border-radius: 4px;
    overflow: hidden;
    box-shadow: 0 10px 28px var(--shadow);
  }

  /* Back of card */
  .card-back {
    left: 150px;
    top: 90px;
    background: var(--card-black);
    display: flex;
    align-items: center;
    justify-content: center;
  }
  .wordmark {
    display: flex;
    align-items: center;
    gap: 18px;
  }
  .wordmark-square {
    width: 46px;
    height: 46px;
    background: var(--crimson);
  }
  .wordmark-name {
    font-weight: 900;
    font-size: 40px;
    letter-spacing: 0.04em;
    line-height: 1;
  }
  .card-back .wordmark-name { color: var(--card-white); }

  /* Front of card */
  .card-front {
    left: 490px;
    top: 468px;
    background: var(--card-white);
  }
  .front-waves {
    position: absolute;
    inset: 0;
  }
  .wave-dark { fill: var(--card-black); }
  .wave-accent { fill: var(--crimson); }

  .card-front .wordmark {
    position: absolute;
    left: 300px;
    top: 58px;
    gap: 12px;
  }
  .card-front .wordmark-square { width: 30px; height: 30px; }
  .card-front .wordmark-name {
    color: var(--ink);
    font-size: 28px;
  }

  .holder {
    position: absolute;
    left: 46px;
    top: 58px;
  }
  .holder-name {
    color: var(--crimson);
    font-weight: 900;
    font-size: 19px;
    letter-spacing: 0.03em;
    text-transform: uppercase;
  }
  .holder-role {
    color: var(--ink-soft);
    font-size: 14px;
    margin: 3px 0 0 8px;
  }

  .contact {
    position: absolute;
    left: 46px;
    top: 176px;
    color: var(--ink);
    font-size: 16px;
    list-style: none;
  }
  .contact-line {
    display: flex;
    align-items: center;
    gap: 8px;
    line-height: 24px;
  }
  .contact-icon { width: 14px; height: 14px; fill: var(--crimson); flex: none; }
  .address {
    font-style: normal;
    margin-top: 12px;
    line-height: 22px;
    font-size: 16.5px;
  }

  .website {
    position: absolute;
    right: 30px;
    top: 242px;
    color: var(--card-white);
    font-size: 13px;
  }
</style>
</head>
<body>
<main class="canvas">

  <section class="card card-back" aria-label="Card back">
    <div class="wordmark">
      <span class="wordmark-square"></span>
      <span class="wordmark-name">KVT LEGAL</span>
    </div>
  </section>

  <section class="card card-front" aria-label="Card front">
    <svg class="front-waves" viewBox="0 0 560 342" preserveAspectRatio="none" aria-hidden="true">
      <path class="wave-dark" d="M0,342 L0,318 C170,318 390,270 560,150 L560,342 Z"/>
      <path class="wave-accent" d="M0,290 C170,296 360,258 490,196 C370,268 180,306 0,308 Z"/>
    </svg>

    <div class="wordmark">
      <span class="wordmark-square"></span>
      <span class="wordmark-name">KVT LEGAL</span>
    </div>

    <div class="holder">
      <p class="holder-name">Boris Telemark</p>
      <p class="holder-role">Partner</p>
    </div>

    <ul class="contact">
      <li class="contact-line">
        <svg class="contact-icon" viewBox="0 0 16 16" aria-hidden="true"><path d="M3 2h3l1.5 3.5-2 1.2a8 8 0 0 0 3.8 3.8l1.2-2L14 10v3a1 1 0 0 1-1 1A11 11 0 0 1 2 3a1 1 0 0 1 1-1z"/></svg>
        <span>0438 715 642</span>
      </li>
      <li class="contact-line">
        <svg class="contact-icon" viewBox="0 0 16 16" aria-hidden="true"><path d="M1 3h14v10H1z M1.8 3.6 8 8.6l6.2-5" stroke="#fff" stroke-width="1.2"/></svg>
        <span>boris@kvtlaw.co</span>
      </li>
      <li>
        <address class="address">Level 3, 118 Wexbury<br>Street, Sydney NSW 2000</address>
      </li>
    </ul>

    <p class="website">www.kvtlaw.co</p>
  </section>

</main>
</body>
</html>
```